Holiday Rental Leaflet

Want a DL size double sided leaflet to distribute via local businesses, markets, family and friends
HOLIDAY RENTALCarrickalinga - 17 Brindle Street Sleeps 8-10 (2 Queen, 1 Double, 2 bunks), 4 bedrooms, BIR to all bedrooms 2 Bathrooms, one with bath, 2 toilets Open Plan Lounge/Dining/Kitchen area Dining Table for 8 peopleReverse cycle airconditionerSlow combustion wood heaterTV/DVD, CD/RadioKitchen has m/wave, oven, fridge/freezer, dishwasherBBQ providedTimber decking with 2 outside tables and 12 chairs Washing Machine and dryer provided One street back from beach Smoke free zone No Pets
For further information or to book contact Joan on 0491 287 306 or email joanfarrow27@velmarnet.com.au

Industry/Entity Type

Kitchen

Requirements
Nice to have
• Have sent a variety of photos of the house. No need to use all of them, pick out the most relevant for the leaflet.

```html
<!DOCTYPE html>
<html lang="en">
<head>
<meta charset="utf-8">
<title>Carrickalinga Holiday Rental Leaflet</title>
<link href="https://fonts.googleapis.com/css2?family=Comfortaa:wght@700&family=Questrial&family=Oswald:wght@600&family=Arimo:wght@700&display=swap" rel="stylesheet">
<style>
  :root {
    --page-bg: #2f2822;
    --sea-top: #4f7089;
    --sea-mid: #6d8ea3;
    --hedge: #4f6d3a;
    --brand-red: #d9452b;
    --card-gold: #e8a81f;
    --paper-white: #ffffff;
    --photo-tone: #8c9a86;
    --family-light: #ead9c6;
    --family-dark: #c9ab8e;
  }
  html, body {
    margin: 0;
    width: 1200px;
    height: 900px;
    overflow: hidden;
    background: var(--page-bg);
  }
  .leaflet {
    position: absolute;
    left: 40px;
    top: 53px;
    width: 1120px;
    height: 794px;
    display: block;
  }
  .title { font-family: "Comfortaa", sans-serif; font-weight: 700; fill: var(--paper-white); }
  .address { font-family: "Questrial", sans-serif; fill: var(--paper-white); }
  .card-heading { font-family: "Oswald", sans-serif; font-weight: 600; fill: var(--paper-white); text-anchor: middle; }
  .card-note { font-family: "Arimo", sans-serif; font-weight: 700; fill: var(--paper-white); text-anchor: middle; }
  .feature-line { font-family: "Comfortaa", sans-serif; font-weight: 700; fill: var(--paper-white); }
  .feature-sub { font-family: "Arimo", sans-serif; font-weight: 700; fill: var(--paper-white); letter-spacing: 2px; }
  .booking { font-family: "Arimo", sans-serif; font-weight: 700; fill: var(--brand-red); text-anchor: middle; }
</style>
</head>
<body>
<svg class="leaflet" viewBox="0 0 1000 710" xmlns="http://www.w3.org/2000/svg">
  <defs>
    <linearGradient id="coastGradient" x1="0" y1="0" x2="1" y2="0.6">
      <stop offset="0" stop-color="var(--sea-top)"/>
      <stop offset="0.6" stop-color="var(--sea-mid)"/>
      <stop offset="0.75" stop-color="var(--hedge)"/>
      <stop offset="1" stop-color="var(--hedge)"/>
    </linearGradient>
    <linearGradient id="familyGradient" x1="0" y1="0" x2="1" y2="1">
      <stop offset="0" stop-color="var(--family-light)"/>
      <stop offset="1" stop-color="var(--family-dark)"/>
    </linearGradient>
  </defs>

  <rect class="coast-photo" x="0" y="0" width="1000" height="710" fill="url(#coastGradient)" role="img" aria-label="Photo of the sea and coastal garden hedges seen from the house"/>

  <path class="feature-band" d="M0,335 C120,315 260,340 420,325 C600,308 780,335 1000,300 L1000,710 L0,710 Z" fill="var(--brand-red)"/>
  <path class="band-edge" d="M470,710 L470,676 C540,662 580,690 630,680 C700,660 770,692 840,672 C905,655 950,690 1000,676 L1000,710 Z" fill="var(--paper-white)"/>

  <g class="feature-card">
    <circle cx="187" cy="260" r="90" fill="var(--paper-white)"/>
    <rect x="37" y="292" width="306" height="262" rx="62" fill="var(--paper-white)"/>
    <circle cx="187" cy="260" r="82" fill="var(--card-gold)"/>
    <rect x="45" y="300" width="290" height="246" rx="55" fill="var(--card-gold)"/>
    <circle cx="187" cy="260" r="68" fill="var(--photo-tone)" stroke="var(--paper-white)" stroke-width="3" role="img" aria-label="Photo of the house with timber decking and garden umbrellas"/>
    <text class="card-heading" x="190" y="392" font-size="40">SLEEPS 8-10</text>
  </g>

  <g class="feature-card">
    <circle cx="502" cy="260" r="90" fill="var(--paper-white)"/>
    <rect x="357" y="292" width="301" height="276" rx="62" fill="var(--paper-white)"/>
    <circle cx="502" cy="260" r="82" fill="var(--card-gold)"/>
    <rect x="365" y="300" width="285" height="260" rx="55" fill="var(--card-gold)"/>
    <circle cx="502" cy="260" r="68" fill="#9a8470" stroke="var(--paper-white)" stroke-width="3" role="img" aria-label="Photo of the slow combustion wood heater against a stone wall"/>
    <text class="card-heading" x="507" y="386" font-size="42">BIR TO ALL</text>
    <text class="card-heading" x="507" y="430" font-size="42">BEDROOMS</text>
    <text class="card-note" x="507" y="461" font-size="15">2 BATHROOMS, ONE</text>
    <text class="card-note" x="507" y="482" font-size="15">WITH BATH, 2 TOILETS</text>
  </g>

  <g class="feature-card">
    <circle cx="817" cy="260" r="90" fill="var(--paper-white)"/>
    <rect x="667" y="292" width="306" height="276" rx="62" fill="var(--paper-white)"/>
    <circle cx="817" cy="260" r="82" fill="var(--card-gold)"/>
    <rect x="675" y="300" width="290" height="260" rx="55" fill="var(--card-gold)"/>
    <circle cx="817" cy="260" r="68" fill="#8f9a88" stroke="var(--paper-white)" stroke-width="3" role="img" aria-label="Photo of the two-storey house front with driveway and lawn"/>
    <text class="card-heading" x="822" y="386" font-size="42">OPEN PLAN</text>
    <text class="card-heading" x="822" y="428" font-size="42">LOUNGE/DINI</text>
    <text class="card-heading" x="822" y="470" font-size="42">NG/KITCHEN</text>
    <text class="card-heading" x="822" y="512" font-size="42">AREA</text>
  </g>

  <path class="family-photo" d="M0,415 C70,392 160,398 205,445 C250,468 305,462 345,492 C385,520 440,518 468,560 C492,600 492,660 478,710 L0,710 Z" fill="url(#familyGradient)" stroke="var(--paper-white)" stroke-width="8" role="img" aria-label="Photo of a smiling family of four"/>

  <text class="title" x="23" y="95" font-size="60" textLength="447" lengthAdjust="spacingAndGlyphs">CARRICKALINGA</text>
  <text class="address" x="470" y="133" font-size="33" text-anchor="end">17 Brindle Street</text>

  <text class="feature-line" x="512" y="632" font-size="30" textLength="463" lengthAdjust="spacingAndGlyphs">DINING TABLE FOR 8 PEOPLE</text>
  <text class="feature-sub" x="512" y="652" font-size="13" textLength="463" lengthAdjust="spacingAndGlyphs">REVERSE CYCLE AIRCONDITIONER</text>

  <text class="booking" x="740" y="700" font-size="11">To book contact Joan on 0491 287 306 or joanfarrow27@velmarnet.com.au</text>
</svg>
</body>
</html>
```